Speech Pathology card for parents of young children

I need a professional, yet fun card for my speech and language pathology services.
I'm trying to offer my speech therapy services to parents of young children. These parents will most likely be women. I want the card to have a fun feel to it and have a concept of speech and language in it (kind of like the cartoon I've attached below showing a boy/girl talking).

I'd want a white background on the card and to bring in some bright colors as well.

Please include the NOVRE logo in a smaller size on a free corner of the card.

Target Market(s)

parents of young children

Contact Information for Business Card

must have my information and I'd like it to have the NOVRE logo (small) somewhere in the corner)

Font styles to use
Serif
Sans Serif

Colors

Designer to choose colors to be used in the design.

Requirements
Must have
• The card title should read: Speech-Language Pathologist
• Lorena Tuvell
• MS CCC-SLP/TSSLD (this under the name)
• 555 014 2786
• lorentuvell@quillpost.net
Nice to have
• i'm looking for a card with a white background and a fun icon that encompasses speaking... similar to the one I've attached.

```html
<!DOCTYPE html>
<html lang="en">
<head>
<meta charset="utf-8">
<title>Speech-Language Pathologist – Business Card</title>
<link href="https://fonts.googleapis.com/css2?family=Ubuntu:wght@300;400;500&display=swap" rel="stylesheet">
<style>
  :root {
    --magenta: #d8237e;
    --magenta-soft: #e0579c;
    --sky: #2fa3d4;
    --sky-soft: #5fb8de;
    --ink: #2a2a2e;
    --paper: #ffffff;
    --backdrop: #efebe4;
  }
  * { box-sizing: border-box; margin: 0; padding: 0; }
  html, body { width: 1200px; height: 942px; overflow: hidden; }
  body {
    background: var(--backdrop);
    font-family: "Ubuntu", sans-serif;
    position: relative;
  }
  .card {
    position: absolute;
    top: 316px;
    width: 540px;
    height: 310px;
    border-radius: 4px;
    overflow: hidden;
    box-shadow: 0 6px 18px rgba(0,0,0,.12);
  }
  .title-block {
    position: absolute;
    display: flex;
    align-items: center;
    gap: 12px;
  }
  .title-dot { width: 18px; height: 18px; border-radius: 50%; flex: none; }
  .card-title { font-weight: 400; line-height: 1.2; }

  /* ---------- front ---------- */
  .card-front { left: 30px; background: var(--paper); }
  .card-front .title-block { left: 40px; top: 76px; width: 240px; }
  .card-front .title-dot { background: var(--magenta); }
  .card-front .card-title { font-size: 22px; color: var(--ink); }
  .divider {
    position: absolute; left: 292px; top: 48px; width: 1.5px; height: 170px;
    background: var(--sky);
  }
  .contact { position: absolute; left: 316px; top: 62px; }
  .person-name { font-size: 25px; font-weight: 400; color: var(--ink); }
  .credentials { margin-top: 4px; font-size: 15px; color: var(--magenta); letter-spacing: .3px; }
  .contact-line {
    display: flex; align-items: center; gap: 9px;
    margin-top: 10px; font-size: 14px; color: var(--ink);
  }
  .contact-line:first-of-type { margin-top: 16px; }
  .contact-line svg { width: 15px; height: 15px; flex: none; }
  .affiliation {
    position: absolute; right: 26px; bottom: 50px;
    display: flex; align-items: center; gap: 8px;
  }
  .affiliation-dot { width: 26px; height: 26px; border-radius: 50%; background: var(--ink); }
  .affiliation-name { font-size: 13px; font-weight: 500; color: var(--ink); letter-spacing: 1px; }
  .accent-band { position: absolute; left: 0; bottom: 0; width: 100%; height: 30px; }

  /* ---------- back ---------- */
  .card-back {
    left: 630px;
    background: linear-gradient(135deg, var(--magenta) 0%, #c77bb0 45%, #8aa3cf 70%, var(--sky) 100%);
  }
  .back-glow {
    position: absolute; right: -60px; bottom: -90px; width: 300px; height: 220px;
    border-radius: 50%; background: rgba(60,170,215,.45);
  }
  .card-back .title-block { left: 0; right: 0; top: 126px; justify-content: center; }
  .card-back .title-dot { background: var(--paper); width: 22px; height: 22px; }
  .card-back .card-title { font-size: 28px; color: var(--paper); }
</style>
</head>
<body>

<section class="card card-front">
  <div class="title-block">
    <span class="title-dot"></span>
    <h1 class="card-title">Speech-Language<br>Pathologist</h1>
  </div>
  <div class="divider"></div>
  <div class="contact">
    <p class="person-name">Lorena Tuvell</p>
    <p class="credentials">MS CCC-SLP/TSSLD</p>
    <p class="contact-line">
      <svg viewBox="0 0 16 16" aria-hidden="true"><rect x="1" y="1" width="14" height="14" rx="3" fill="var(--sky)"/><path d="M5 4.5c0 4 2.5 6.5 6.5 6.5l.5-1.8-2-.8-.9.9C7.8 8.6 7.4 8.2 6.7 6.9l.9-.9-.8-2z" fill="#fff"/></svg>
      555 014 2786
    </p>
    <p class="contact-line">
      <svg viewBox="0 0 16 16" aria-hidden="true"><rect x="1" y="3" width="14" height="10" rx="1.5" fill="var(--sky)"/><path d="M1.8 4l6.2 5 6.2-5" stroke="#fff" stroke-width="1.3" fill="none"/></svg>
      lorentuvell@quillpost.net
    </p>
  </div>
  <div class="affiliation">
    <span class="affiliation-dot"></span>
    <span class="affiliation-name">NOVRE</span>
  </div>
  <svg class="accent-band" viewBox="0 0 540 30" preserveAspectRatio="none" aria-hidden="true">
    <polygon points="0,0 325,0 305,30 0,30" fill="var(--magenta-soft)"/>
    <polygon points="329,0 540,0 540,30 309,30" fill="var(--sky-soft)"/>
  </svg>
</section>

<section class="card card-back">
  <div class="back-glow"></div>
  <div class="title-block">
    <span class="title-dot"></span>
    <h2 class="card-title">Speech-Language<br>Pathologist</h2>
  </div>
</section>

</body>
</html>
```